BRCW Business Cards

Business Cards should contain:
Bright Ridgecrest Coating Works
Felix Darrow
M: 0417 865 093
E: brightRCW@fernpost.example
BRCW logo
TCG logo
Painting & Decorating
Licence # 719362K
slogan: See the shine of a careful finish

Target Market(s)

all aspect of painting

Industry/Entity Type

Trade

Contact Information for Business Card

Felix Darrow
M: 0417 865 093
E: brightRCW@fernpost.example
BRCW logo
TCG logo
Painting & Decorating
Licence # 719362K

Font styles to use
Serif
Sans Serif

Requirements
Must have
• clear design with nice backround
• two sides
• smal TCG logo
Nice to have
• easy to read
Should not have
• mess
• black
• plastics form

```html
<!DOCTYPE html>
<html lang="en">
<head>
<meta charset="utf-8">
<title>BRCW Business Cards</title>
<link rel="stylesheet" href="https://fonts.googleapis.com/css2?family=Lustria&family=Open+Sans:wght@400;600;700&display=swap">
<style>
  :root {
    --teal: #1a5656;
    --teal-dark: #134646;
    --green: #4a9a3a;
    --ink: #3a3a3a;
    --paper: #ffffff;
    --backdrop: #e9e6e1;
    --serif: "Lustria", Georgia, serif;
    --sans: "Open Sans", Arial, sans-serif;
  }
  * { box-sizing: border-box; margin: 0; padding: 0; }
  html, body { width: 1200px; height: 1023px; overflow: hidden; }
  body { background: var(--backdrop); position: relative; font-family: var(--sans); }

  .card {
    position: absolute;
    width: 560px;
    height: 340px;
    border-radius: 4px;
    box-shadow: 0 6px 18px rgba(0,0,0,0.18);
    overflow: hidden;
  }
  .card--front { left: 80px; top: 140px; background: var(--paper); border-right: 14px solid var(--teal); }
  .card--back { left: 560px; top: 540px; background: var(--teal); color: var(--paper); }

  /* brand lockup */
  .lockup { position: absolute; display: flex; align-items: center; gap: 16px; }
  .lockup__mark { width: 58px; height: 58px; border-radius: 50%; flex: none; }
  .lockup__text { display: flex; flex-direction: column; }
  .lockup__name { font-family: var(--serif); font-size: 54px; line-height: 1; letter-spacing: 1px; }
  .lockup__rule { height: 1px; margin: 6px 0 4px; }
  .lockup__line { font-family: var(--serif); font-size: 17px; line-height: 1.2; }

  .card--front .lockup { left: 34px; top: 36px; }
  .card--front .lockup__mark { background: var(--green); }
  .card--front .lockup__name { color: var(--teal); }
  .card--front .lockup__rule { background: var(--teal); }
  .card--front .lockup__line--first { color: var(--green); }
  .card--front .lockup__line--second { color: var(--teal); }

  .person { position: absolute; left: 34px; top: 170px; }
  .person__name { font-size: 20px; font-weight: 700; color: var(--teal); }
  .person__role { font-size: 13px; color: var(--green); }

  .contact { position: absolute; left: 34px; bottom: 30px; list-style: none; font-size: 13px; color: var(--ink); }
  .contact li { display: flex; align-items: center; gap: 8px; line-height: 1.55; }
  .contact svg { width: 12px; height: 12px; fill: var(--teal); flex: none; }

  .licence { position: absolute; right: 26px; bottom: 30px; text-align: left; font-size: 13px; color: var(--ink); line-height: 1.55; }

  .card--back .lockup { right: 40px; bottom: 44px; }
  .card--back .lockup__mark { background: var(--paper); }
  .card--back .lockup__rule { background: var(--paper); }

  .partner-badge {
    position: absolute; left: 40px; top: 40px;
    width: 110px; height: 80px;
    border: 2px solid var(--paper); border-radius: 6px;
  }
</style>
</head>
<body>

<section class="card card--front" aria-label="Business card front">
  <div class="lockup">
    <span class="lockup__mark"></span>
    <div class="lockup__text">
      <span class="lockup__name">BRCW</span>
      <span class="lockup__rule"></span>
      <span class="lockup__line lockup__line--first">Bright Ridgecrest</span>
      <span class="lockup__line lockup__line--second">Coating Works</span>
    </div>
  </div>

  <div class="person">
    <p class="person__name">Felix Darrow</p>
    <p class="person__role">Painter</p>
  </div>

  <ul class="contact">
    <li><svg viewBox="0 0 24 24" aria-hidden="true"><path d="M6.6 10.8a15 15 0 0 0 6.6 6.6l2.2-2.2a1 1 0 0 1 1-.25 11.4 11.4 0 0 0 3.6.57 1 1 0 0 1 1 1V20a1 1 0 0 1-1 1A17 17 0 0 1 3 4a1 1 0 0 1 1-1h3.5a1 1 0 0 1 1 1c0 1.25.2 2.45.57 3.57a1 1 0 0 1-.25 1z"/></svg>0417 865 093</li>
    <li><svg viewBox="0 0 24 24" aria-hidden="true"><path d="M2 5h20v14H2z"/><path d="M2 5l10 8 10-8" fill="none" stroke="#ffffff" stroke-width="2"/></svg>brightRCW@fernpost.example</li>
    <li><svg viewBox="0 0 24 24" aria-hidden="true"><circle cx="12" cy="12" r="10"/></svg>www.brightRCW.example</li>
  </ul>

  <div class="licence">
    <p>Licence&nbsp; no # 719362K</p>
    <p>See the shine of a careful finish</p>
  </div>
</section>

<section class="card card--back" aria-label="Business card back">
  <div class="partner-badge" role="img" aria-label="Partner association badge"></div>
  <div class="lockup">
    <span class="lockup__mark"></span>
    <div class="lockup__text">
      <span class="lockup__name">BRCW</span>
      <span class="lockup__rule"></span>
      <span class="lockup__line">Bright Ridgecrest</span>
      <span class="lockup__line">Coating Works</span>
    </div>
  </div>
</section>

</body>
</html>
```